Business Cards

Simple but professional looking business cards

Name: Rina Tolvardi
Title: Principle Cloud Systems Consultant
Email: r@kbrx.net.au
web : www.kbrx.net.au
Phone: +61.8.95203417
Mobile: +61.431862055
Updates

Hi All, Please include the office address Level 1, 200 Quarrington St, Carrowmere, KV, 7021

Industry/Entity Type

Business

```html
<!DOCTYPE html>
<html lang="en">
<head>
<meta charset="utf-8">
<title>KBRX Business Cards</title>
<link rel="stylesheet" href="https://fonts.googleapis.com/css2?family=Tinos:ital,wght@0,400;1,400&display=swap">
<style>
  :root {
    --backdrop: #9a9a99;
    --card-blue: #0f56a0;
    --card-blue-light: #1c79c4;
    --card-blue-dark: #0c4688;
    --text-light: #d3dbe6;
    --white: #ffffff;
    --brand-blue: #1560a8;
    --badge-dark: #111111;
  }
  * { margin: 0; padding: 0; box-sizing: border-box; }
  html, body { width: 1200px; height: 1000px; overflow: hidden; }
  body {
    background: var(--backdrop);
    font-family: "Tinos", "Times New Roman", serif;
    position: relative;
  }
  .card {
    position: absolute;
    width: 660px;
    height: 377px;
    border-radius: 3px;
    box-shadow: 0 6px 18px rgba(0,0,0,0.25);
    overflow: hidden;
  }
  .card--front {
    left: 480px; top: 60px;
    background: radial-gradient(ellipse at 45% 35%, var(--card-blue-light) 0%, var(--card-blue) 55%, var(--card-blue-dark) 100%);
  }
  .card--contact {
    left: 60px; top: 480px;
    background: linear-gradient(160deg, var(--card-blue) 0%, var(--card-blue-dark) 100%);
  }
  .front-brand {
    position: absolute;
    left: 110px; top: 110px;
    display: flex; align-items: center; gap: 26px;
  }
  .front-brand__mark {
    width: 120px; height: 120px;
    border-radius: 50%;
    background: var(--white);
  }
  .front-brand__name {
    color: var(--white);
    font-size: 120px;
    line-height: 1;
    letter-spacing: 4px;
  }
  .partner-badge {
    position: absolute;
    right: 26px; bottom: 24px;
    width: 180px; height: 54px;
  }
  .card--front .partner-badge { background: var(--badge-dark); }
  .card--contact .partner-badge { background: var(--white); right: 36px; bottom: 30px; width: 200px; height: 62px; }
  .person {
    position: absolute;
    left: 38px; top: 30px;
    color: var(--text-light);
  }
  .person__name { font-size: 30px; line-height: 1.1; }
  .person__title { font-size: 17px; font-style: italic; margin-top: 4px; }
  .office {
    position: absolute;
    left: 38px; top: 115px;
    color: var(--text-light);
    font-size: 18px;
    font-style: normal;
    line-height: 1.5;
  }
  .office__line2 { padding-left: 76px; }
  .contacts {
    position: absolute;
    left: 38px; top: 230px;
    list-style: none;
    color: var(--text-light);
    font-size: 22px;
    line-height: 1.2;
  }
  .logo-panel {
    position: absolute;
    right: 36px; top: 110px;
    width: 236px; height: 116px;
    background: var(--white);
    display: flex; align-items: center; justify-content: center; gap: 14px;
  }
  .logo-panel__mark {
    width: 54px; height: 54px;
    border-radius: 50%;
    background: var(--brand-blue);
  }
  .logo-panel__name {
    color: var(--brand-blue);
    font-size: 54px;
    line-height: 1;
    letter-spacing: 2px;
  }
</style>
</head>
<body>
  <section class="card card--front" aria-label="Business card front">
    <div class="front-brand">
      <span class="front-brand__mark"></span>
      <span class="front-brand__name">KBRX</span>
    </div>
    <div class="partner-badge" role="img" aria-label="Partner badge"></div>
  </section>

  <section class="card card--contact" aria-label="Business card back">
    <div class="person">
      <p class="person__name">Rina Tolvardi</p>
      <p class="person__title">Principle Cloud Systems Consultant</p>
    </div>
    <address class="office">
      <p>Office : Level 1, 200 Quarrington St</p>
      <p class="office__line2">Carrowmere, KV, 7021</p>
    </address>
    <ul class="contacts">
      <li>Email : r@kbrx.net.au</li>
      <li>web : www.kbrx.net.au</li>
      <li>Phone : +61.8.95203417</li>
      <li>Mobile : +61.431862055</li>
    </ul>
    <div class="logo-panel">
      <span class="logo-panel__mark"></span>
      <span class="logo-panel__name">KBRX</span>
    </div>
    <div class="partner-badge" role="img" aria-label="Partner badge"></div>
  </section>
</body>
</html>
```